Harbor Crestline (Business Card Design)

Need business cards designed. Something modern, chic, and sleek. Mabye the back of the card should be the navy blue that is in the logo and then just the logo on the back.

Target Market(s)

Those in the hotel, office, and renovation industry

Contact Information for Business Card

1. Logo 2. Tomasz Ferreiro 3. CEO/Founder 4. Phone: (833) HarbCre / (833) 427-2273 5. Email: tomasz@theharborcrestline.com 6. Website: www.theharborcrestline.com

Font styles to use
Other font styles liked:
• Look at the logo font and base the font for everything else off of that.

Colors
0054AA
0677BA
7BADD7
CADEEF
E8F1F8

Requirements
Must have
• Colors that are associated in the logo
Nice to have
• Sleek modern clean and chic design.

```html
<!DOCTYPE html>
<html lang="en">
<head>
<meta charset="utf-8">
<title>Harbor Crestline — Business Card</title>
<link href="https://fonts.googleapis.com/css2?family=Montserrat:wght@600&family=Poppins:wght@400;600&display=swap" rel="stylesheet">
<style>
  :root {
    --navy: #10183f;
    --gold: #d2a445;
    --ink-grey: #5f5f5f;
    --paper: #ffffff;
    --backdrop: #d9d9d9;
  }
  * { margin: 0; padding: 0; box-sizing: border-box; }
  html, body {
    width: 1200px; height: 959px; overflow: hidden;
    background: var(--backdrop);
  }
  .card {
    position: absolute;
    left: 295px;
    width: 612px;
    height: 352px;
  }
  .card--front { top: 103px; background: var(--paper); }
  .card--back { top: 499px; background: var(--navy); }

  .contact-block {
    position: absolute;
    left: 40px;
    top: 98px;
    font-family: "Poppins", sans-serif;
  }
  .person-name {
    font-weight: 600;
    font-size: 25px;
    line-height: 1;
    color: var(--navy);
  }
  .person-title {
    margin-top: 6px;
    font-size: 14px;
    color: var(--gold);
  }
  .divider {
    width: 10px; height: 1.5px;
    background: var(--navy);
    margin: 20px 0 24px;
  }
  .contact-list { list-style: none; }
  .contact-item {
    display: flex; align-items: center; gap: 5px;
    font-size: 14.6px;
    line-height: 22px;
    color: var(--ink-grey);
  }
  .contact-item svg { width: 13px; height: 13px; flex: none; }

  .brand {
    position: absolute;
    display: flex; flex-direction: column; align-items: center; gap: 14px;
    font-family: "Montserrat", sans-serif;
    font-weight: 600;
    letter-spacing: 1px;
    white-space: nowrap;
  }
  .brand-mark { width: 14px; height: 14px; background: var(--gold); }
  .brand-name { font-size: 26px; }
  .card--front .brand { left: 466px; top: 132px; transform: translateX(-50%); color: var(--navy); }
  .card--back .brand { left: 306px; top: 134px; transform: translateX(-50%); color: var(--paper); }
</style>
</head>
<body>
  <section class="card card--front">
    <div class="contact-block">
      <h1 class="person-name">Tomasz Ferreiro</h1>
      <p class="person-title">CEO/Founder</p>
      <div class="divider"></div>
      <ul class="contact-list">
        <li class="contact-item">
          <svg viewBox="0 0 24 24" aria-hidden="true"><path fill="#10183f" d="M6.6 10.8c1.4 2.8 3.8 5.1 6.6 6.6l2.2-2.2c.3-.3.7-.4 1-.2 1.1.4 2.3.6 3.6.6.6 0 1 .4 1 1V20c0 .6-.4 1-1 1C10.6 21 3 13.4 3 4c0-.6.4-1 1-1h3.5c.6 0 1 .4 1 1 0 1.3.2 2.5.6 3.6.1.3 0 .7-.2 1z"/></svg>
          (833) HarbCre / (833) 427-2273
        </li>
        <li class="contact-item">
          <svg viewBox="0 0 24 24" aria-hidden="true"><rect x="2" y="5" width="20" height="14" fill="#10183f"/><path d="M2 5l10 8 10-8M2 19l8-7M22 19l-8-7" stroke="#fff" stroke-width="1.6" fill="none"/></svg>
          tomasz@theharborcrestline.com
        </li>
        <li class="contact-item">
          <svg viewBox="0 0 24 24" aria-hidden="true"><g fill="none" stroke="#10183f" stroke-width="2"><circle cx="12" cy="12" r="9.5"/><ellipse cx="12" cy="12" rx="4" ry="9.5"/><path d="M2.5 12h19M4 7h16M4 17h16"/></g></svg>
          www.theharborcrestline.com
        </li>
      </ul>
    </div>
    <div class="brand">
      <span class="brand-mark"></span>
      <span class="brand-name">Harbor Crestline</span>
    </div>
  </section>

  <section class="card card--back">
    <div class="brand">
      <span class="brand-mark"></span>
      <span class="brand-name">Harbor Crestline</span>
    </div>
  </section>
</body>
</html>
```